Event for Hair Salon Wigs

We are introducing a new division of our hair salon selling hair wigs. We are introducing our clients to our wig line, which are beautiful well crafted wig. These wigs are not like granny's wigs, but wigs for women who want style and are willing to pay extra for beautiful believeable wigs. The event is casual were clients and there friends will be flowing in and out during a sunday afternoon.
The postcard should reflect a nice sunny spring day, but classy not extremely colorful. If you think a photo would add to a better look to the card....let me know and I will upload some.
Thank you

I have images that was uploaded, but have not been posted to this project. I'm not sure what's going on, but please look out for them. I have been trying to communicate with customer service, but no  response thus far. The cards I have received this far I think have to much of a colored pattern, I would love it if the logo "M Lovely Wigs" took center stage, rather than the word open house. Open House is important, but I don't won't it to be bolder than "wigs." Please leave room for address labels, and if possible, the description of the event should be in little bigger text. Oh, I am open to an abstract lady rather than the images that are uploaded, but if images are used, you don't have to use them all. Believe it or not...I do like simplicity:)

```html
<!DOCTYPE html>
<html lang="en">
<head>
<meta charset="utf-8">
<title>M Lovely Wigs – Open House Postcard</title>
<link href="https://fonts.googleapis.com/css2?family=Satisfy&family=Source+Sans+3:wght@400&display=swap" rel="stylesheet">
<style>
  :root {
    --page-bg: #e8e3de;
    --blossom-deep: #c8244e;
    --blossom-mid: #e0607e;
    --blossom-soft: #f2c3c6;
    --sky-haze: #e9e0dc;
    --plum: #4a1027;
    --plum-dark: #3a0a1e;
    --cream: #f6e7c6;
    --script-red: #e5252e;
    --white: #ffffff;
  }
  * { margin: 0; padding: 0; box-sizing: border-box; }
  html, body { width: 1200px; height: 675px; overflow: hidden; }
  body {
    background: var(--page-bg);
    font-family: "Source Sans 3", "Myriad Pro", sans-serif;
    position: relative;
  }
  .postcard {
    position: absolute;
    top: 125px;
    width: 530px;
    height: 416px;
    box-shadow: 0 6px 18px rgba(0,0,0,0.25);
    overflow: hidden;
  }
  .postcard--front { left: 51px; }
  .postcard--back { left: 623px; background: radial-gradient(ellipse at 40% 40%, var(--plum) 0%, var(--plum-dark) 100%); color: var(--cream); }

  .front-photo {
    position: absolute; inset: 0;
    background:
      radial-gradient(ellipse at 25% 20%, var(--blossom-deep) 0%, transparent 45%),
      radial-gradient(ellipse at 60% 85%, var(--blossom-deep) 0%, transparent 50%),
      radial-gradient(ellipse at 85% 15%, var(--sky-haze) 0%, transparent 45%),
      linear-gradient(160deg, var(--blossom-mid) 0%, var(--blossom-soft) 55%, var(--blossom-mid) 100%);
  }
  .front-brand {
    position: absolute;
    left: 232px; top: 156px;
    font-size: 40px;
    line-height: 1;
    color: var(--white);
    white-space: nowrap;
  }

  .back-title {
    position: absolute; left: 14px; top: 14px;
    font-family: "Satisfy", cursive;
    font-size: 36px; color: var(--script-red); line-height: 1.1;
  }
  .back-date {
    position: absolute; left: 14px; top: 58px;
    font-size: 15px; line-height: 1.1;
  }
  .back-greeting, .back-signoff, .back-extras {
    position: absolute; left: 14px;
    font-family: "Satisfy", cursive; line-height: 1;
  }
  .back-greeting { top: 102px; font-size: 23px; }
  .back-body {
    position: absolute; left: 14px; top: 131px; width: 505px;
    font-size: 13.2px; line-height: 1.2;
  }
  .back-body em { font-style: italic; }
  .back-signoff { top: 260px; font-size: 23px; }
  .back-signer { position: absolute; left: 22px; top: 285px; font-size: 15px; }
  .back-extras { top: 318px; font-size: 24px; }
  .back-contact {
    position: absolute; left: 14px; top: 355px;
    font-size: 13.5px; line-height: 1.35;
  }
  .back-brand {
    position: absolute; right: 16px; top: 368px;
    font-size: 19px; color: var(--script-red); white-space: nowrap;
  }
</style>
</head>
<body>
  <section class="postcard postcard--front">
    <div class="front-photo" role="img" aria-label="Photograph of pink spring blossom branches against a soft blurred background"></div>
    <div class="front-brand">M Lovely Wigs</div>
  </section>

  <section class="postcard postcard--back">
    <h1 class="back-title">Open House</h1>
    <p class="back-date">Sunday April 13th 2014<br>11am to 3pm</p>
    <p class="back-greeting">Hello!</p>
    <p class="back-body">I would like to cordially invite you to <em>Salon Ember</em> to introduce you to <em>M Lovely Wigs</em>. A showroom of some of the finest human and synthetic hair wigs available. Come look, feel and try-on these beautiful wigs. <em>M Lovely Wigs</em> can be purchased and ordered the day of the event for an introductory offer of 10% off of the total sales. If you bring a friend or donate a gently warn wig for charity, you will receive 15% off of the total purchase. Additionally, bring a friend and a gently warn wig and receive 20% off of the total purchase. Come join us…you might find a fabulous new look for spring!</p>
    <p class="back-signoff">Hope to see you,</p>
    <p class="back-signer">Marian Holt</p>
    <p class="back-extras">Light appetizers and Drinks, Raffles</p>
    <p class="back-contact">www.mlovelywigs.com<br>555 014-2287, Salon Ember<br>4820 Harbor View Rd, Ste. B, Lakeside, Ca 90000</p>
    <div class="back-brand">M Lovely Wigs</div>
  </section>
</body>
</html>
```